Business Card Design Project

Please create a custom business card for Birchmoor Links School. The logo is attached to this brief.

Colours could be based on Blue, black, red, or white color. Colors like orange, green, purple, pink are not preferable.

Here is the link to the logo project : http://tasks.artquarrel.net/task.aspx?id=413057

Questions can be posted on the Discussion Board.

```html
<!DOCTYPE html>
<html lang="en">
<head>
<meta charset="utf-8">
<title>Birchmoor Links School – Business Card</title>
<link href="https://fonts.googleapis.com/css2?family=Open+Sans:wght@400;600;700&display=swap" rel="stylesheet">
<style>
  :root {
    --navy: #232a6e;
    --navy-deep: #161b4f;
    --navy-light: #2e3a8f;
    --white: #ffffff;
    --grey: #b9bcc4;
    --backdrop: #e9e7e3;
    --type: "Open Sans", Arial, sans-serif;
  }
  * { box-sizing: border-box; margin: 0; padding: 0; }
  html, body { width: 1200px; height: 900px; overflow: hidden; }
  body {
    background: var(--backdrop);
    font-family: var(--type);
    position: relative;
  }
  .card {
    position: absolute;
    width: 525px;
    height: 300px;
    border-radius: 18px;
    overflow: hidden;
    box-shadow: 0 6px 20px rgba(0,0,0,.18);
  }
  /* Front */
  .card-front { left: 337px; top: 120px; background: var(--white); }
  .card-front .shape { position: absolute; inset: 0; }
  .front-name {
    position: absolute; left: 34px; top: 36px;
    display: flex; align-items: center; gap: 10px;
    color: var(--navy); font-weight: 700; font-size: 26px; letter-spacing: -.3px;
  }
  .mark-dot {
    width: 30px; height: 30px; border-radius: 50%; background: var(--navy);
  }
  .address {
    position: absolute; left: 30px; top: 150px;
    color: var(--white); font-size: 13px; line-height: 18px;
  }
  .contact {
    position: absolute; right: 28px; top: 178px;
    color: var(--white); text-align: right;
  }
  .person { font-weight: 700; font-size: 16px; line-height: 20px; }
  .role { font-size: 12px; line-height: 16px; margin-bottom: 6px; }
  .line {
    display: flex; justify-content: flex-end; align-items: center; gap: 6px;
    font-size: 12.5px; line-height: 17px; font-weight: 600;
  }
  .line svg { width: 12px; height: 12px; flex: none; }
  /* Back */
  .card-back {
    left: 337px; top: 480px;
    background: radial-gradient(circle at 55% 35%, var(--navy-light), var(--navy) 55%, var(--navy-deep));
    color: var(--white);
  }
  .back-name {
    position: absolute; left: 0; right: 0; top: 118px;
    display: flex; justify-content: center; align-items: center; gap: 12px;
    font-weight: 700; font-size: 32px; letter-spacing: -.3px;
  }
  .back-name .mark-dot { width: 40px; height: 40px; background: var(--white); }
  .back-url {
    position: absolute; left: 0; right: 0; top: 180px;
    text-align: center; font-size: 15px; letter-spacing: 2.5px;
  }
</style>
</head>
<body>

<section class="card card-front" aria-label="Business card front">
  <svg class="shape" viewBox="0 0 525 300" width="525" height="300">
    <path d="M0 118 C170 150 360 182 525 168 L525 300 L0 300 Z" fill="var(--navy)"/>
    <path d="M250 162 C350 168 450 162 525 150 L525 160 C440 172 340 174 250 162 Z" fill="var(--grey)"/>
  </svg>
  <div class="front-name"><span class="mark-dot"></span>Birchmoor Links School</div>
  <p class="address">4100 Fenwick Rd<br>Larkford TX 70000</p>
  <div class="contact">
    <p class="person">Calum Rennard</p>
    <p class="role">Manager</p>
    <p class="line">555 014 2270
      <svg viewBox="0 0 12 12"><circle cx="6" cy="6" r="6" fill="#fff"/><path d="M4 3 L5 3 L5.5 4.5 L4.8 5 Q5.5 6.8 7 7.2 L7.5 6.5 L9 7 L9 8 Q6 9 3.5 5 Q3.3 3.5 4 3Z" fill="var(--navy)"/></svg></p>
    <p class="line">555 014 2271
      <svg viewBox="0 0 12 12"><circle cx="6" cy="6" r="6" fill="#fff"/><rect x="3" y="4.5" width="6" height="4" rx="1" fill="var(--navy)"/><rect x="4" y="3" width="4" height="1.5" fill="var(--navy)"/></svg></p>
    <p class="line">info@BirchmoorLinks.com
      <svg viewBox="0 0 12 12"><circle cx="6" cy="6" r="6" fill="#fff"/><rect x="3" y="4" width="6" height="4" fill="var(--navy)"/><path d="M3 4 L6 6.3 L9 4" stroke="#fff" stroke-width=".7" fill="none"/></svg></p>
    <p class="line">www.BirchmoorLinks.com
      <svg viewBox="0 0 12 12"><circle cx="6" cy="6" r="6" fill="#fff"/><circle cx="6" cy="6" r="3.2" fill="none" stroke="var(--navy)" stroke-width=".8"/><path d="M2.8 6 H9.2 M6 2.8 V9.2" stroke="var(--navy)" stroke-width=".8"/></svg></p>
  </div>
</section>

<section class="card card-back" aria-label="Business card back">
  <div class="back-name"><span class="mark-dot"></span>Birchmoor Links School</div>
  <p class="back-url">www.BirchmoorLinks.com</p>
</section>

</body>
</html>
```